Ferncrest Dental, LLC business card project

Business card to be designed with current logo.
Dental office- please keep design of card that looks clean and professional.
Please include the following info:
Ferncrest Dental, LLC
Dr. Lorna Pettigrew
2871 Marlowe Street
Bethlehem, PA 18093
610-555-0193
ferncrestdental.office@examplemail.test
Hello everyone-
Reason: Just got back from overseas- will look at all designs and provide feedback. Thank you!
Reason: Polling my friends for the final selection-
thank you to all those that participated- so many talented designers!

```html
<!DOCTYPE html>
<html lang="en">
<head>
<meta charset="utf-8">
<title>Ferncrest Dental, LLC – Business Card</title>
<link rel="stylesheet" href="https://fonts.googleapis.com/css2?family=Arimo:wght@400;700&display=swap">
<style>
  :root {
    --card-bg: #ffffff;
    --frame: #1a1a1a;
    --brand-green: #6aa844;
    --leaf-green: #b5d334;
    --contact-grey: #bcbcbc;
  }
  * { margin: 0; padding: 0; box-sizing: border-box; }
  html, body {
    width: 1200px;
    height: 686px;
    overflow: hidden;
    background: var(--card-bg);
  }
  .card {
    position: relative;
    width: 1200px;
    height: 686px;
    background: var(--card-bg);
    border: 2px solid var(--frame);
    font-family: "Arimo", Arial, sans-serif;
  }
  .brand {
    position: absolute;
    left: 50px;
    top: 150px;
    width: 1100px;
    display: flex;
    align-items: center;
    justify-content: space-between;
  }
  .brand-dot {
    width: 96px;
    height: 96px;
    border-radius: 50%;
    background: var(--leaf-green);
    flex: none;
  }
  .brand-name {
    font-size: 70px;
    font-weight: 400;
    color: var(--brand-green);
    letter-spacing: -1px;
    white-space: nowrap;
  }
  .divider {
    position: absolute;
    left: 812px;
    top: 292px;
    width: 326px;
    height: 6px;
  }
  .contact {
    position: absolute;
    right: 52px;
    top: 338px;
    text-align: right;
  }
  .doctor {
    font-size: 38px;
    font-weight: 700;
    color: var(--brand-green);
    line-height: 48px;
    margin-bottom: 38px;
  }
  .contact-line {
    font-size: 36px;
    color: var(--contact-grey);
    line-height: 51.5px;
    white-space: nowrap;
  }
</style>
</head>
<body>
  <div class="card">
    <div class="brand">
      <div class="brand-dot"></div>
      <div class="brand-name">Ferncrest Dental, LLC</div>
    </div>

    <svg class="divider" viewBox="0 0 326 6" aria-hidden="true">
      <line x1="3" y1="3" x2="323" y2="3" stroke="var(--leaf-green)" stroke-width="4" stroke-linecap="round" stroke-dasharray="0 19.9"/>
    </svg>

    <div class="contact">
      <p class="doctor">Dr. Lorna Pettigrew</p>
      <p class="contact-line">2871 Marlowe Street</p>
      <p class="contact-line">Bethlehem, PA 18093</p>
      <p class="contact-line">610-555-0193</p>
      <p class="contact-line">ferncrestdental.office@examplemail.test</p>
    </div>
  </div>
</body>
</html>
```